Business card for different employees

A professional new updated design incorporating our current business's color themes and styles such as our on-site service trucks decals included in pictures attached. Our current business card is very simple and not professionally designed. We are a small family business but want a professional corporate look.

Target Market(s)

Cards to be handed out to new customers , corperate meetings. For our on site service operators.

Industry/Entity Type

Hydraulic

Contact Information for Business Card

Address, website, phone number, email, logo.
slogan - "Industry chosen hose and fittings provider".
24/7 on-site service , supply and hose management
Experienced , indpendant , family owned

Font styles to use
Sans Serif

Requirements
Must have
• Easily editable so that I can add different names and different roles for employees etc.
Nice to have
• Freedom with colour doesn't necessarily have to be blue but that is our company colour theme with trucks and logo so makes sense for the card to have blue like the trucks.

```html
<!DOCTYPE html>
<html lang="en">
<head>
<meta charset="utf-8">
<title>Torrent Hose and Fittings – Business Card</title>
<link rel="stylesheet" href="https://fonts.googleapis.com/css2?family=Jost:wght@400;500&family=Poppins:wght@600;700&display=swap">
<style>
  :root{
    --brand-blue:#1330c4;
    --ink:#1a1a1a;
    --text-grey:#4a4a4a;
    --card-white:#ffffff;
    --backdrop:#e9e9ec;
    --fitting-light:#d6d6d6;
    --fitting-dark:#8a8a8a;
  }
  *{margin:0;padding:0;box-sizing:border-box}
  html,body{width:1125px;height:1200px;overflow:hidden;background:var(--backdrop)}
  body{position:relative;font-family:"Jost",sans-serif}

  .card{position:absolute;left:162px;width:800px;height:456px;border-radius:28px;overflow:hidden;
        box-shadow:0 4px 10px rgba(0,0,0,.25)}
  .card--front{top:103px;background:var(--card-white)}
  .card--back{top:620px;background:var(--brand-blue)}

  /* front */
  .brand-name{position:absolute;left:47px;top:74px;width:72px;color:var(--ink);
              font:500 15px/22px "Jost",sans-serif;letter-spacing:.2px}
  .name-bar{position:absolute;left:124px;top:60px;width:282px;height:29px;background:var(--brand-blue);
            color:#fff;font:500 21px/29px "Jost",sans-serif;padding-left:26px;letter-spacing:.3px}
  .role-bar{position:absolute;left:124px;top:89px;width:238px;height:22px;background:var(--ink);
            color:#fff;font:400 14px/22px "Jost",sans-serif;padding-left:26px}
  .fitting{position:absolute;left:362px;top:90px;width:44px;height:18px;border-radius:2px;
           background:linear-gradient(var(--fitting-light),var(--fitting-dark))}
  .contact{position:absolute;left:47px;color:var(--text-grey);font-size:18px;line-height:22px}
  .contact--address{top:281px}
  .contact--lines{top:342px}
  .services{position:absolute;right:49px;top:342px;text-align:right;color:var(--text-grey);font-size:18px;line-height:23px}

  /* back */
  .lockup{position:absolute;left:156px;top:170px;display:flex;align-items:center;gap:14px}
  .lockup__dot{width:104px;height:104px;border-radius:50%;background:#fff}
  .lockup__name{color:#fff;font:700 44px/1 "Poppins",sans-serif;letter-spacing:1px}
  .lockup__name small{display:block;font-size:18px;line-height:22px;letter-spacing:3px;margin-top:4px}
  .tagline{position:absolute;left:253px;top:262px;color:#fff;font:600 20px/26px "Poppins",sans-serif}
</style>
</head>
<body>
  <section class="card card--front">
    <p class="brand-name">TORRENT</p>
    <div class="name-bar">DANIEL REEVE</div>
    <div class="role-bar">PRESIDENT</div>
    <div class="fitting" role="img" aria-label="Hose fitting illustration"></div>
    <p class="contact contact--address">1420 Harbour Road<br>Westfield, Alaska 34012</p>
    <p class="contact contact--lines">P. 0400 555 219<br>info@torrenthose.com.au<br>www.torrenthose.com.au</p>
    <p class="services">24/7 On-Site Service<br>Supply &amp;Hose Management<br>Experienced |Independant | Family owned</p>
  </section>

  <section class="card card--back">
    <div class="lockup">
      <div class="lockup__dot"></div>
      <div class="lockup__name">TORRENT<small>HOSE AND FITTINGS</small></div>
    </div>
    <p class="tagline">Industry chosen hose &amp; fittings provider</p>
  </section>
</body>
</html>
```